Piano genealogy graphs template, for a large poster printing

Hello and thank you for your interest in my project.
I need a poster template, so I can create structures similar to the one I have uploaded. I want to completely replace or improve my poor previous design which is attached.
I need to be able to input names and dates into boxes of various colors, arrows pointing between boxes. I would also like to be able to label each graph (not each box).
I am looking at something that would be legible when printed, in a one consistent professional layout of 2A0 (around 1189x1682 mm) poster (I know it is large). The design template required here can include just few sample text boxes with sample flags on a suitable background, for me to multiply later and spread across the whole poster.
The positioning of the boxes is not important.
Please let me know if more clarification is required.
Thank you for your help.

Feel free to follow what I have attached in the file, or change the design completely.

UPDATE 4/12: I have uploaded two more graphs as an example. At this stage of the contest, I would like to have one of those graphs done, and I am planning to offer a 'freelance job' to one or two designers, who will be willing to do the whole 10 graphs on one poster.

Reason: Dear Designers, Since the project is rather complex and large-scale, I have decided to give everyone more time to work on their designs. I will consider extending it further if any of you require additional time. Best wishes, leopold

Dear Designers, I would like to inform you that the contest for my poster is now closed and that I have assigned the prizes. I would like to thank all of you for submiting your high-quality designs, and for your participation. It was a great pleasure working with all of you. Due to the large size of the project itself (large number of graphs to be fitted on a single poster), I had to focus on providing feedback to only those designers who provided projects closest to what I was expecting at the early stages of the contest. I wish you all the best for the future, Kind regards, Leopold

Target Market(s)

Pianists, historians

Industry/Entity Type

Printing

Requirements
Must have
• Consistent design, but allow to clearly delineate various genealogy trees.

```html
<!DOCTYPE html>
<html lang="en">
<head>
<meta charset="utf-8">
<title>Card Four – French Tree</title>
<link rel="stylesheet" href="https://fonts.googleapis.com/css2?family=Open+Sans:ital,wght@0,400;0,700;1,700&family=Ubuntu:wght@700&family=Fredoka:wght@600&display=swap">
<style>
:root{
  --backdrop:#eeeeee;
  --paper:#ffffff;
  --ink:#1f1f1f;
  --box:#262626;
  --box-text:#ffffff;
  --year:#b5b5b5;
  --accent:#e8273b;
  --line:#c9c9c9;
  --flag-blue:#1f3a93;
  --flag-white:#ffffff;
  --flag-red:#e8273b;
}
*{box-sizing:border-box;margin:0;padding:0}
html,body{width:1200px;height:1000px;overflow:hidden}
body{background:var(--backdrop);position:relative;font-family:"Open Sans",Arial,sans-serif}
.poster{position:absolute;left:279px;top:47px;width:642px;height:908px;background:var(--paper)}
.card-title{position:absolute;left:233px;top:56px;font:700 36px/1 "Ubuntu",Arial,sans-serif;color:var(--ink);letter-spacing:.5px}
.brand{position:absolute;left:462px;top:30px;width:154px;font:700 21px/1.2 "Ubuntu",Arial,sans-serif;color:var(--ink);text-align:left;padding-left:16px}
.branch-banner{position:absolute;left:20px;top:150px}
.connectors{position:absolute;left:0;top:0}
.teacher{position:absolute;width:137px;background:var(--box);color:var(--box-text);border-radius:0 16px 0 16px;padding:5px 8px 6px 7px}
.teacher-name{display:flex;align-items:center;gap:7px;font:italic 700 7.6px/1.2 "Open Sans",Arial,sans-serif}
.teacher.solo{height:30px;padding-top:0;padding-bottom:0;display:flex;align-items:center;padding-left:18px}
.flag{display:inline-block;width:13px;height:9px;flex:none;background:linear-gradient(90deg,var(--flag-blue) 0 33.3%,var(--flag-white) 33.3% 66.6%,var(--flag-red) 66.6%)}
.students-label{font:700 4px/1 "Open Sans",Arial,sans-serif;letter-spacing:.3px;margin:2px 0 1px 20px}
.students{list-style:none;margin-left:20px;font-size:6.3px;line-height:7.7px}
.students span{color:var(--year)}
</style>
</head>
<body>
<main class="poster">
  <h1 class="card-title">CARD FOUR</h1>
  <div class="brand">KEYSTONE<br>PIANO<br>ACADEMIES</div>

  <svg class="branch-banner" width="400" height="95" viewBox="0 0 400 95">
    <polygon points="55,6 290,6 306,47 290,87 55,87" fill="var(--accent)"/>
    <polygon points="312,6 370,6 390,47 370,87 312,87 328,47" fill="var(--accent)"/>
    <rect x="334" y="32" width="30" height="28" rx="3" fill="var(--paper)" role="img" aria-label="Grand piano icon"/>
    <circle cx="55" cy="47" r="43" fill="var(--paper)" stroke="var(--accent)" stroke-width="6"/>
    <text x="55" y="30" text-anchor="middle" font-family="Fredoka, sans-serif" font-weight="600" font-size="11" fill="var(--accent)">BRANCH</text>
    <text x="55" y="74" text-anchor="middle" font-family="Fredoka, sans-serif" font-weight="600" font-size="42" fill="var(--accent)">1</text>
    <text x="114" y="56" font-family="Fredoka, sans-serif" font-weight="600" font-size="25" fill="var(--paper)">French Tree</text>
  </svg>

  <svg class="connectors" width="642" height="908" viewBox="279 47 642 908" fill="none" stroke="var(--line)" stroke-width="1">
    <path d="M372 397V415H522M522 402V432M672 402V428H827V412M597 428V500M522 462V508M441 530H490V550H508M630 486V550H645M827 486V500H672V550H645M713 600H680V680H645M577 605V634M441 650H490V668H508M577 731V760M408 732V745H745V732M577 790V814"/>
    <g fill="var(--accent)" stroke="none">
      <circle cx="372" cy="405" r="1.6"/><circle cx="522" cy="422" r="1.6"/><circle cx="672" cy="418" r="1.6"/>
      <circle cx="827" cy="420" r="1.6"/><circle cx="597" cy="480" r="1.6"/><circle cx="522" cy="485" r="1.6"/>
      <circle cx="456" cy="530" r="1.6"/><circle cx="630" cy="495" r="1.6"/><circle cx="656" cy="550" r="1.6"/>
      <circle cx="704" cy="600" r="1.6"/><circle cx="577" cy="620" r="1.6"/><circle cx="454" cy="650" r="1.6"/>
      <circle cx="577" cy="745" r="1.6"/><circle cx="408" cy="740" r="1.6"/><circle cx="745" cy="740" r="1.6"/>
      <circle cx="577" cy="802" r="1.6"/>
    </g>
  </svg>

  <article class="teacher" style="left:25px;top:303px">
    <h2 class="teacher-name"><i class="flag"></i>Henri Valmont (1916-2008)</h2>
    <p class="students-label">STUDENTS:</p>
    <ul class="students"><li>Jean-Luc Morand <span>(1948)</span></li><li>Jacques Vautrin <span>(1947)</span></li><li>Jean-Marc Pellerin <span>(1944)</span></li></ul>
  </article>

  <article class="teacher" style="left:175px;top:303px">
    <h2 class="teacher-name"><i class="flag"></i>Odile Marchand (1906)</h2>
    <p class="students-label">STUDENTS:</p>
    <ul class="students"><li>Jean-Yves Ribaud <span>(1961)</span></li><li>Mireille Lasalle <span>(1952)</span></li><li>Pascal Renaud <span>(1951)</span></li><li>Katia Lasalle <span>(1950)</span></li></ul>
  </article>

  <article class="teacher" style="left:325px;top:303px">
    <h2 class="teacher-name"><i class="flag"></i>Luc Ferrand (1907-1982)</h2>
    <p class="students-label">STUDENTS:</p>
    <ul class="students"><li>Inès Baret <span>(1941)</span></li><li>Mireille Lasalle <span>(1940)</span></li><li>Dominique Merval <span>(1938)</span></li><li>Philippe Estoril <span>(1934)</span></li></ul>
  </article>

  <article class="teacher" style="left:480px;top:303px">
    <h2 class="teacher-name"><i class="flag"></i>Simone Delacour (1924-2010)</h2>
    <p class="students-label">STUDENTS:</p>
    <ul class="students"><li>Nicolas Andrieu <span>(1970)</span></li><li>Pierre-Louis Aubert <span>(1957)</span></li><li>Peter Dunmore <span>(1953)</span></li><li>Michel Besson <span>(1950)</span></li><li>Paul Crossfield <span>(1944)</span></li></ul>
  </article>

  <article class="teacher" style="left:25px;top:385px">
    <h2 class="teacher-name"><i class="flag"></i>Simone Delacour (1924-2010)</h2>
    <p class="students-label">STUDENTS:</p>
    <ul class="students"><li>Nicolas Andrieu <span>(1970)</span></li><li>Pierre-Louis Aubert <span>(1957)</span></li><li>Peter Dunmore <span>(1953)</span></li><li>Michel Besson <span>(1950)</span></li><li>Paul Crossfield <span>(1944)</span></li><li>Jean-Luc Morand <span>(1948)</span></li><li>Jacques Vautrin <span>(1947)</span></li><li>Jean-Marc Pellerin <span>(1944)</span></li><li>Jean-Yves Ribaud <span>(1961)</span></li><li>Mireille Lasalle <span>(1952)</span></li><li>Pascal Renaud <span>(1951)</span></li><li>Katia Lasalle <span>(1950)</span></li><li>Peter Dunmore <span>(1953)</span></li><li>Michel Besson <span>(1950)</span></li><li>Mireille Lasalle <span>(1952)</span></li></ul>
  </article>

  <article class="teacher solo" style="left:175px;top:385px">
    <h2 class="teacher-name"><i class="flag"></i>Marcel Aubry (1890-1956)</h2>
  </article>

  <article class="teacher" style="left:325px;top:385px">
    <h2 class="teacher-name"><i class="flag"></i>Odile Marchand (1906)</h2>
    <p class="students-label">STUDENTS:</p>
    <ul class="students"><li>Jean-Yves Ribaud <span>(1961)</span></li><li>Mireille Lasalle <span>(1952)</span></li><li>Pascal Renaud <span>(1951)</span></li><li>Katia Lasalle <span>(1950)</span></li></ul>
  </article>

  <article class="teacher" style="left:480px;top:385px">
    <h2 class="teacher-name"><i class="flag"></i>Odile Marchand (1906)</h2>
    <p class="students-label">STUDENTS:</p>
    <ul class="students"><li>Jean-Yves Ribaud <span>(1961)</span></li><li>Mireille Lasalle <span>(1952)</span></li><li>Pascal Renaud <span>(1951)</span></li><li>Katia Lasalle <span>(1950)</span></li></ul>
  </article>

  <article class="teacher" style="left:229px;top:461px">
    <h2 class="teacher-name"><i class="flag"></i>Simone Delacour (1924-2010)</h2>
    <p class="students-label">STUDENTS:</p>
    <ul class="students"><li>Nicolas Andrieu <span>(1970)</span></li><li>Pierre-Louis Aubert <span>(1957)</span></li><li>Peter Dunmore <span>(1953)</span></li><li>Michel Besson <span>(1950)</span></li><li>Paul Crossfield <span>(1944)</span></li><li>Jean-Luc Morand <span>(1948)</span></li><li>Jacques Vautrin <span>(1947)</span></li><li>Jean-Marc Pellerin <span>(1944)</span></li><li>Jean-Yves Ribaud <span>(1961)</span></li><li>Mireille Lasalle <span>(1952)</span></li></ul>
  </article>

  <article class="teacher" style="left:434px;top:477px">
    <h2 class="teacher-name"><i class="flag"></i>Simone Delacour (1924-2010)</h2>
    <p class="students-label">STUDENTS:</p>
    <ul class="students"><li>Nicolas Andrieu <span>(1970)</span></li><li>Pierre-Louis Aubert <span>(1957)</span></li><li>Peter Dunmore <span>(1953)</span></li><li>Michel Besson <span>(1950)</span></li><li>Paul Crossfield <span>(1944)</span></li><li>Jean-Luc Morand <span>(1948)</span></li><li>Jacques Vautrin <span>(1947)</span></li><li>Jean-Marc Pellerin <span>(1944)</span></li><li>Jean-Yves Ribaud <span>(1961)</span></li><li>Mireille Lasalle <span>(1952)</span></li><li>Pascal Renaud <span>(1951)</span></li><li>Katia Lasalle <span>(1950)</span></li><li>Peter Dunmore <span>(1953)</span></li><li>Michel Besson <span>(1950)</span></li><li>Mireille Lasalle <span>(1952)</span></li></ul>
  </article>

  <article class="teacher" style="left:25px;top:561px">
    <h2 class="teacher-name"><i class="flag"></i>Simone Delacour (1924-2010)</h2>
    <p class="students-label">STUDENTS:</p>
    <ul class="students"><li>Nicolas Andrieu <span>(1970)</span></li><li>Pierre-Louis Aubert <span>(1957)</span></li><li>Peter Dunmore <span>(1953)</span></li><li>Michel Besson <span>(1950)</span></li><li>Paul Crossfield <span>(1944)</span></li></ul>
  </article>

  <article class="teacher" style="left:229px;top:587px">
    <h2 class="teacher-name"><i class="flag"></i>Simone Delacour (1924-2010)</h2>
    <p class="students-label">STUDENTS:</p>
    <ul class="students"><li>Nicolas Andrieu <span>(1970)</span></li><li>Pierre-Louis Aubert <span>(1957)</span></li><li>Peter Dunmore <span>(1953)</span></li><li>Michel Besson <span>(1950)</span></li><li>Paul Crossfield <span>(1944)</span></li><li>Jean-Luc Morand <span>(1948)</span></li><li>Jacques Vautrin <span>(1947)</span></li><li>Jean-Marc Pellerin <span>(1944)</span></li><li>Jean-Yves Ribaud <span>(1961)</span></li><li>Mireille Lasalle <span>(1952)</span></li></ul>
  </article>

  <article class="teacher solo" style="left:63px;top:655px">
    <h2 class="teacher-name"><i class="flag"></i>Marcel Aubry (1890-1956)</h2>
  </article>
  <article class="teacher solo" style="left:394px;top:655px">
    <h2 class="teacher-name"><i class="flag"></i>Marcel Aubry (1890-1956)</h2>
  </article>
  <article class="teacher solo" style="left:236px;top:713px">
    <h2 class="teacher-name"><i class="flag"></i>Marcel Aubry (1890-1956)</h2>
  </article>
  <article class="teacher solo" style="left:236px;top:767px">
    <h2 class="teacher-name"><i class="flag"></i>Marcel Aubry (1890-1956)</h2>
  </article>
</main>
</body>
</html>
```